brindle's business card for earthmoving and tipper hire business.

I have a small earthmoving and tipper truck company. I am aiming for the smaller jobs that the big guys don't want. I am also Doing grass slashing and fire hazard reduction work. I would like to see some earthy colors, greens browns etc. I have a tractor with a front end loader attachment, and a 22 ton tipper. I would like to maybe have a silhouette of a tipper and tractor/slasher/loader setup in centre with my business name over the top and details to one side or something like that

Industry/Entity Type

Business

Contact Information for Business Card

Brindle's small earthworks and tipper hireToowoombaABN: 47781050480PH 0479126773Email brindle.4@fenwickmail.com

Font styles to use
Sans Serif

Colors
fbee3d
abd036
85cae6
f78f20

Requirements
Nice to have
• Earthy colors . business name in blue

```html
<!DOCTYPE html>
<html lang="en">
<head>
<meta charset="utf-8">
<title>Brindle's Small Earthworks and Tipper Hire – Business Card</title>
<link href="https://fonts.googleapis.com/css2?family=Fira+Sans+Condensed:wght@700&family=Saira:wght@400&display=swap" rel="stylesheet">
<style>
  :root {
    --backdrop: #ececec;
    --charcoal: #2b2b2b;
    --sky-blue: #56c5f0;
    --field-green: #aecb60;
    --ember-orange: #f07a18;
    --sun-yellow: #f5e71a;
    --chalk: #ffffff;
    --machine-tone: #e6e6e6;
    --ink: #2c2c2c;
  }
  * { margin: 0; padding: 0; box-sizing: border-box; }
  html, body {
    width: 1200px;
    height: 819px;
    overflow: hidden;
    background: var(--backdrop);
  }
  .card {
    position: absolute;
    left: 50px;
    top: 91px;
    width: 1100px;
    height: 636px;
    background: var(--field-green);
    overflow: hidden;
  }
  .card__header {
    position: absolute;
    left: 0; top: 0;
    width: 100%;
    height: 334px;
    background: var(--charcoal);
  }
  .card__stripe {
    position: absolute;
    left: 0;
    width: 100%;
  }
  .card__stripe--orange { top: 334px; height: 9px; background: var(--ember-orange); }
  .card__stripe--yellow { top: 343px; height: 9px; background: var(--sun-yellow); }

  .business-name {
    position: absolute;
    z-index: 2;
    left: 0; top: 35px;
    width: 100%;
    text-align: center;
    font-family: "Fira Sans Condensed", sans-serif;
    font-weight: 700;
    font-size: 56px;
    line-height: 70px;
    letter-spacing: 1.5px;
    color: var(--sky-blue);
    text-transform: uppercase;
  }
  .machine {
    position: absolute;
    z-index: 1;
    background: linear-gradient(180deg, var(--machine-tone), #bdbdbd);
    border-radius: 6px;
  }
  .machine--tipper { left: 119px; top: 172px; width: 212px; height: 157px; }
  .machine--loader { left: 760px; top: 176px; width: 212px; height: 153px; }

  .abn {
    position: absolute;
    left: 406px; top: 246px;
    font-family: "Saira", sans-serif;
    font-size: 26px;
    line-height: 36px;
    color: var(--chalk);
    letter-spacing: 0.8px;
  }

  .contact-list {
    position: absolute;
    left: 104px; top: 426px;
    list-style: none;
    font-family: "Saira", sans-serif;
    font-size: 34px;
    color: var(--ink);
  }
  .contact-list li {
    display: flex;
    align-items: center;
    height: 47px;
    letter-spacing: 1.8px;
  }
  .contact-list svg {
    width: 32px;
    height: 32px;
    margin-right: 17px;
    fill: var(--ink);
    flex: none;
  }

  .service-list {
    position: absolute;
    left: 649px; top: 372px;
    list-style: none;
    font-family: "Saira", sans-serif;
    font-size: 31px;
    line-height: 40px;
    letter-spacing: 0.8px;
    color: var(--ink);
  }
  .service-list li::before {
    content: "";
    display: inline-block;
    width: 9px;
    height: 9px;
    border-radius: 50%;
    background: var(--ink);
    margin-right: 12px;
    vertical-align: middle;
    position: relative;
    top: -3px;
  }
</style>
</head>
<body>
  <div class="card">
    <div class="card__header"></div>
    <div class="card__stripe card__stripe--orange"></div>
    <div class="card__stripe card__stripe--yellow"></div>

    <div class="machine machine--tipper" role="img" aria-label="White silhouette of a tipper truck with its tray raised"></div>
    <div class="machine machine--loader" role="img" aria-label="White silhouette of a skid steer loader with bucket"></div>

    <h1 class="business-name">Brindle's Small Earthworks<br>and Tipper Hire</h1>

    <p class="abn">ABN: 62194038715</p>

    <ul class="contact-list">
      <li>
        <svg viewBox="0 0 24 24" aria-hidden="true"><path d="M6.6 10.8c1.4 2.8 3.8 5.1 6.6 6.6l2.2-2.2c.3-.3.7-.4 1-.2 1.1.4 2.3.6 3.6.6.6 0 1 .4 1 1V20c0 .6-.4 1-1 1C10.6 21 3 13.4 3 4c0-.6.4-1 1-1h3.5c.6 0 1 .4 1 1 0 1.3.2 2.5.6 3.6.1.3 0 .7-.2 1L6.6 10.8z"/></svg>
        0438571629
      </li>
      <li>
        <svg viewBox="0 0 24 24" aria-hidden="true"><path d="M2 5h20v14H2V5zm2 2v.4l8 5.2 8-5.2V7H4zm16 2.8-8 5.2-8-5.2V17h16V9.8z"/></svg>
        brindle.4@fenwickmail.com
      </li>
      <li>
        <svg viewBox="0 0 24 24" aria-hidden="true"><path d="M12 2a7 7 0 0 0-7 7c0 5.2 7 13 7 13s7-7.8 7-13a7 7 0 0 0-7-7zm0 9.5A2.5 2.5 0 1 1 12 6.5a2.5 2.5 0 0 1 0 5z"/></svg>
        Toowoomba
      </li>
    </ul>

    <ul class="service-list">
      <li>Small earthworks</li>
      <li>Slashing</li>
      <li>Fire hazard reduction</li>
      <li>Rural cleanups</li>
      <li>Tipper</li>
    </ul>
  </div>
</body>
</html>
```